Business Card Design for an Investment Company

We need a business card design for our private investment company, called Dunmore Equity. Dunmore Equity is an investments partnership that aims to acquire shares in listed companies with a view to influencing those companies through active dialogue in order to improve their value. We need designs that use the logo colors (blue, grey, white), we need both English and Arabic on the business cards (can be on one side or 2 sides). The final logo should communicate professionalism, conservatism (nothing too fancy or too cheesy), that we are smart, conservative and old school.

Target Market(s)

Investment companies

Industry/Entity Type

Investment

Contact Information for Business Card

Tariq Salmanuddin Farouqi
Senior Executive Officer

Harbor Court 07, Level 3, Office 214/12
QTFZ

+9714987650
tfarouqi@dunmore-equity.com
www.dunmore-equity.com

Requirements
Must have
• Logo to be placed on the left hand side of the business card
• for the Arabic, we only need to have the name and title so it can be accomodated on one side so we can have the other side with full color and logo. The arabic that needs to be used is the below:
• طارق سلمان الدين فاروقي
• المدير التنفيدي

```html
<!DOCTYPE html>
<html lang="en">
<head>
<meta charset="utf-8">
<title>Dunmore Equity – Business Card</title>
<link href="https://fonts.googleapis.com/css2?family=Montserrat:wght@400;500;700;800&family=Cairo:wght@500;700&display=swap" rel="stylesheet">
<style>
  :root {
    --brand-blue: #1d6d9c;
    --brand-grey: #5a5a5c;
    --text-grey: #6b6b6e;
    --rule-grey: #8a8a8c;
    --card-white: #f2f2f2;
    --stage: #e4e4e2;
  }
  * { box-sizing: border-box; margin: 0; padding: 0; }
  html, body {
    width: 1200px; height: 900px; overflow: hidden;
    background: var(--stage);
    font-family: "Montserrat", Arial, sans-serif;
  }
  .sheet {
    width: 1200px; height: 900px;
    display: flex; flex-direction: column;
    align-items: center; justify-content: center; gap: 56px;
  }
  .card {
    position: relative;
    width: 620px; height: 354px;
    box-shadow: 0 6px 18px rgba(0,0,0,0.14);
  }
  /* Front: contact side */
  .card--front { background: var(--card-white); }
  .wordmark {
    font-weight: 800;
    letter-spacing: -0.5px;
    white-space: nowrap;
  }
  .card--front .wordmark {
    position: absolute; left: 42px; top: 40px;
    font-size: 38px; color: var(--brand-blue);
  }
  .holder {
    position: absolute; left: 42px; top: 122px;
  }
  .holder__name {
    font-size: 17px; font-weight: 700; color: var(--brand-grey);
  }
  .holder__title {
    margin-top: 3px; font-size: 14px; font-weight: 500; color: var(--brand-blue);
  }
  .holder--arabic {
    left: auto; right: 42px; top: 118px;
    direction: rtl; text-align: right;
    font-family: "Cairo", "Noto Sans Arabic", sans-serif;
  }
  .holder--arabic .holder__name { font-size: 18px; }
  .holder--arabic .holder__title { margin-top: 0; font-size: 14px; }
  .divider {
    position: absolute; left: 42px; top: 178px;
    width: 360px; height: 1px; background: var(--rule-grey);
  }
  .contacts {
    position: absolute; left: 42px; top: 192px;
    list-style: none;
  }
  .contacts li {
    display: flex; align-items: center; gap: 8px;
    font-size: 12px; color: var(--text-grey);
    height: 21px; white-space: nowrap;
  }
  .contacts svg { width: 12px; height: 12px; flex: none; }
  .address {
    position: absolute; left: 262px; top: 194px;
    font-size: 12px; line-height: 19px; color: var(--text-grey);
    font-style: normal; white-space: nowrap;
  }
  /* Back: brand side */
  .card--back { background: var(--brand-blue); }
  .card--back .wordmark {
    position: absolute; right: 46px; bottom: 52px;
    font-size: 34px; color: #ffffff;
  }
</style>
</head>
<body>
<main class="sheet">
  <section class="card card--front" aria-label="Business card, contact side">
    <div class="wordmark">Dunmore Equity</div>

    <div class="holder">
      <p class="holder__name">Tariq Salmanuddin Farouqi</p>
      <p class="holder__title">Senior Executive Officer</p>
    </div>

    <div class="holder holder--arabic" lang="ar">
      <p class="holder__name">طارق سلمان الدين فاروقي</p>
      <p class="holder__title">المدير التنفيدي</p>
    </div>

    <div class="divider"></div>

    <ul class="contacts">
      <li>
        <svg viewBox="0 0 12 12" aria-hidden="true">
          <circle cx="6" cy="6" r="5.4" fill="none" stroke="#1d6d9c" stroke-width="1"/>
          <path d="M4.2 3.3l1 1.1-.6.8c.4.8 1 1.4 1.8 1.8l.8-.6 1.1 1-.6.9c-2.2-.3-3.9-2-4.2-4.2z" fill="#1d6d9c"/>
        </svg>
        +9714987650
      </li>
      <li>
        <svg viewBox="0 0 12 12" aria-hidden="true">
          <rect x="1" y="2.5" width="10" height="7" fill="none" stroke="#1d6d9c" stroke-width="1"/>
          <path d="M1 2.8l5 3.8 5-3.8" fill="none" stroke="#1d6d9c" stroke-width="1"/>
        </svg>
        tfarouqi@dunmore-equity.com
      </li>
      <li>
        <svg viewBox="0 0 12 12" aria-hidden="true">
          <circle cx="6" cy="6" r="5.4" fill="#1d6d9c"/>
          <ellipse cx="6" cy="6" rx="2.2" ry="5" fill="none" stroke="#fff" stroke-width=".8"/>
          <path d="M1 6h10M2 3.5h8M2 8.5h8" stroke="#fff" stroke-width=".8"/>
        </svg>
        www.dunmore-equity.com
      </li>
    </ul>

    <address class="address">
      Harbor Court 07, Level 3,<br>
      Office 214/12<br>
      QTFZ
    </address>
  </section>

  <section class="card card--back" aria-label="Business card, brand side">
    <div class="wordmark">Dunmore Equity</div>
  </section>
</main>
</body>
</html>
```